Business Card Design

I need a business card and logo for a new company based in Manhattan, Kansas called "Ferncliff Works, LLC". I am a project management consultant. I specialize in laying the foundation for businesses and business owners to get their projects on track. Think of it as if you were wanting to go from coast to coast on a train. Before you can jump on the train and sell tickets, you have to design the path the train will take, acquire the land, clear the trees, level the ground, prepare the base for the track, lay the track and finally place the train on the track (That's what I do with my clients). Once the train is on the track and I've provided them with the operations manual, then they and their managers get to drive the train. I don't have color preferences. The final design should communicate a clear direction or path to growing the customer's business.
Updates

Since I am in need of a logo as well, I have also created a logo design project that will work in conjunction with this project.

Reason: Accepted a company logo this afternoon that I would like to have cards designed around. Sorry for jumping the gun and posting both projects at the same time.

Industry/Entity Type

Business

Contact Information for Business Card

Owner: Dale Purvis. Business Name: Ferncliff Works, LLC. Business Address: 4871 Marlow Bend, Manhattan, KS, 66921. Business Phone Number: 785-640-1572. Business Email: dale@ferncliffworksllc.example

```html
<!DOCTYPE html>
<html lang="en">
<head>
<meta charset="utf-8">
<title>Ferncliff Works, LLC — Business Card</title>
<link rel="stylesheet" href="https://fonts.googleapis.com/css2?family=Carlito:wght@400;700&display=swap">
<style>
  :root {
    --band-blue: #a2b3d1;
    --panel-light: #f3f4f7;
    --accent-red: #ec1c24;
    --text-white: #ffffff;
  }
  html, body {
    margin: 0;
    padding: 0;
    overflow: hidden;
    background: #ffffff;
  }
  .card {
    position: relative;
    width: 1200px;
    height: 703px;
    background: var(--band-blue);
    font-family: "Carlito", "Calibri", sans-serif;
    overflow: hidden;
  }
  .header-panel {
    position: absolute;
    left: 0;
    top: 26px;
    width: 1200px;
    height: 266px;
    background: var(--panel-light);
  }
  .company-name,
  .logo-slot,
  .contact-text,
  .address {
    position: absolute;
    margin: 0;
    line-height: 1;
    white-space: nowrap;
  }
  .company-name {
    left: 91px;
    top: 132px;
    font-size: 38px;
    font-weight: 700;
    color: var(--accent-red);
  }
  .logo-slot {
    left: 804px;
    top: 138px;
    font-size: 31px;
    font-weight: 400;
    color: var(--accent-red);
  }
  .bullet {
    position: absolute;
    left: 74px;
    width: 31px;
    height: 31px;
    background: var(--accent-red);
  }
  .contact-text {
    left: 131px;
    font-weight: 700;
    color: var(--text-white);
    font-size: 31px;
  }
  .contact-text.owner { top: 352px; font-size: 38px; }
  .contact-text.phone { top: 438px; }
  .contact-text.email { top: 499px; }
  .divider {
    position: absolute;
    top: 611px;
    height: 3px;
    background: var(--text-white);
  }
  .divider.left { left: 24px; width: 522px; }
  .divider.right { left: 652px; width: 524px; }
  .home-icon {
    position: absolute;
    left: 569px;
    top: 573px;
    width: 60px;
    height: 56px;
  }
  .address {
    left: 0;
    width: 1212px;
    text-align: center;
    top: 641px;
    font-size: 31px;
    font-weight: 700;
    color: var(--text-white);
  }
</style>
</head>
<body>
  <div class="card">
    <div class="header-panel" role="img" aria-label="Light dotted texture background"></div>
    <p class="company-name">Ferncliff Works, LLC</p>
    <p class="logo-slot">Your logo here</p>

    <span class="bullet" style="top:355px"></span>
    <p class="contact-text owner">Dale Purvis</p>

    <span class="bullet" style="top:433px"></span>
    <p class="contact-text phone">785-640-1572</p>

    <span class="bullet" style="top:502px"></span>
    <p class="contact-text email">dale@ferncliffworksllc.example</p>

    <span class="divider left"></span>
    <svg class="home-icon" viewBox="0 0 60 56" aria-hidden="true">
      <path d="M30 2 L2 26 L8 31 L30 12 L52 31 L58 26 Z" fill="#ec1c24"/>
      <path d="M10 30 L30 14 L50 30 L50 56 L36 56 L36 40 L24 40 L24 56 L10 56 Z" fill="#ec1c24"/>
    </svg>
    <span class="divider right"></span>

    <p class="address">4871 Marlow Bend, Manhattan, KS, 66921</p>
  </div>
</body>
</html>
```